KVR Associates needs a web site

We need a web site for www.kvrassociates-example.com. KVR is a mergers and acquisition consulting company that focuses our buyer and seller services on logistics companies. We help put companies together, and help with legal and financial due diligence. We want the web site to express our service and show the logistics components. We want personalized images versus pictures of trucks and airplanes.

Our new logo uses Burgandy and grey colors. Image attached. We are not in to bold, big letters...classy, artistic, low key preferred. Confidentiality, experience, professional are what we want to express on the site.

All we expect for the first part of this project is a home page, and one subpage.  We are budgeting other funds for the technical aspects of the web site

Reason: All that I'm seeing so far is trucks, forklifts and planes. We are a legal mergers and acquisitions firm that focus on logistics. I like some of the images to say logistics, but really want it say legal, financial, and putting companies together. Will pay extra for the sub page if someone can impress us with a home page.

Reason: Swamped with another project at the moment...will work on this over the weekend and provide designer feedback and select final design by Tuesday

```html
<!DOCTYPE html>
<html lang="en">
<head>
<meta charset="utf-8">
<title>KVR Associates</title>
<link href="https://fonts.googleapis.com/css2?family=Open+Sans:wght@300;400;600&display=swap" rel="stylesheet">
<style>
:root{
  --burgundy:#a3103a;
  --burgundy-dark:#8a0d2f;
  --grey-dark:#2b2b2b;
  --grey-text:#7a7a7a;
  --grey-light:#9c9c9c;
  --hero-blue:#c9d3e6;
  --purple-line:#7b7aa0;
  --link-blue:#3e4a86;
  --footer:#333335;
}
*{margin:0;padding:0;box-sizing:border-box}
html,body{width:984px;height:1200px;overflow:hidden;background:#fff}
body{position:relative;font-family:"Open Sans",Arial,sans-serif;color:var(--grey-text)}
.abs{position:absolute}

.brand{left:89px;top:38px;display:flex;align-items:center;gap:10px}
.brand-mark{width:14px;height:14px;background:var(--burgundy)}
.brand-name{font-size:26px;font-weight:400;color:var(--grey-dark);letter-spacing:1px}

.phone{right:92px;top:26px;font-size:12px;color:#555}
.phone strong{font-size:19px;font-weight:400;color:var(--burgundy)}
.search{left:590px;top:60px;width:152px;height:23px;border:1px solid #c9c9c9;font-size:10px;color:#666;padding:4px 7px;display:flex;justify-content:space-between;align-items:center}
.social{left:755px;top:57px;display:flex;gap:4px}
.social span{width:31px;height:31px;border-radius:50%;background:#9aa0ab}
.social span:nth-child(2){background:var(--burgundy)}

.nav{left:0;top:122px;width:984px;height:35px;background:linear-gradient(#a8143c,var(--burgundy-dark));display:flex;padding-left:80px}
.nav a{color:#fff;text-decoration:none;font-size:12px;line-height:35px;padding:0 16px;border-right:1px solid rgba(255,255,255,.25)}
.nav a:last-child{border-right:0}

.hero{left:0;top:157px;width:984px;height:438px;background:linear-gradient(90deg,#2d3556 0%,#6a6f8c 18%,#c3cde2 38%,var(--hero-blue) 100%)}
.quote-top{left:622px;top:276px;width:272px;height:40px;background:var(--grey-dark)}
.quote-mid{left:388px;top:316px;width:506px;height:42px;background:var(--grey-dark)}
.quote-text{right:90px;top:283px;text-align:right;color:#fff;font-size:23px;line-height:35px;font-weight:600}
.quote-text .light{font-weight:300}
.quote-sub{left:407px;top:358px;width:487px;height:43px;background:rgba(163,16,58,.85);color:#fff;font-size:13px;line-height:43px;padding-left:9px}
.more{left:786px;top:408px;width:108px;height:37px;background:#fff;border-bottom:2px solid var(--burgundy);color:var(--burgundy);font-size:11.5px;line-height:35px;text-align:center}
.dots{left:853px;top:461px;display:flex;gap:7px;align-items:center}
.dots i{width:7px;height:7px;border-radius:50%;background:var(--burgundy)}
.dots i:first-child{width:11px;height:11px;background:#333}

.center{left:95px;top:563px;width:805px;height:302px;background:#fff;border:1px solid #e4e4e4;border-bottom:5px solid var(--purple-line);box-shadow:0 1px 4px rgba(0,0,0,.08)}
.center h2{position:absolute;top:20px;width:100%;text-align:center;font-weight:300;font-size:25px;color:var(--burgundy)}
.service{position:absolute;top:73px;width:238px}
.service .pic{height:119px;border-radius:2px}
.service h3{font-size:11.5px;font-weight:400;color:var(--burgundy);margin-top:13px;letter-spacing:-.3px;line-height:16px}
.service p{font-size:9.6px;line-height:14px;color:var(--grey-light);margin-top:7px;letter-spacing:-.1px}
.service p.compact{font-size:8.4px;letter-spacing:-.25px}
.service a{display:block;font-size:10.5px;line-height:14px;color:var(--link-blue);text-decoration:none;margin-top:7px}

.section-title{font-size:22px;font-weight:300;color:var(--burgundy);line-height:30px}
.welcome{left:94px;top:898px;width:532px}
.welcome p{font-size:10.9px;line-height:19.7px;font-weight:300;color:#666;margin-top:7px;letter-spacing:-.15px}
.welcome p+p{margin-top:19px}
.btn{display:inline-block;background:var(--burgundy);color:#fff;font-size:11.5px;padding:0 6px;height:23px;line-height:23px;text-decoration:none}
.welcome .btn{margin-top:14px;margin-left:2px}

.testimonials{left:676px;top:898px;width:214px}
.testimonial{display:flex;gap:9px;margin-top:26px}
.testimonial+.testimonial{margin-top:12px}
.avatar{width:47px;height:47px;flex:none;background:linear-gradient(#d9d4cf,#b9aea5)}
.testimonial p{font-size:10px;line-height:15px;color:#555;letter-spacing:-.1px}
.testimonial .name{font-size:12px;color:var(--burgundy);font-weight:600;margin-top:6px}
.testimonials .btn{margin-top:35px}

.footer{left:0;top:1160px;width:984px;height:40px;background:var(--footer);color:#9a9a9a;font-size:10.5px}
.footer .copy{position:absolute;left:90px;top:12px}
.footer .follow{position:absolute;right:90px;top:7px;display:flex;align-items:center;gap:8px}
.footer .follow span{display:inline-block;width:25px;height:25px;background:#3e5a9a}
.footer .follow span:nth-of-type(2){background:#2c5d8c}
.footer .follow span:nth-of-type(3){background:#3fa9dc}
</style>
</head>
<body>

<header>
  <div class="abs brand"><span class="brand-mark"></span><span class="brand-name">KVR Associates</span></div>
  <div class="abs phone">Call: <strong>555.014.2290</strong></div>
  <div class="abs search">Search
    <svg width="11" height="11" viewBox="0 0 11 11"><circle cx="4.5" cy="4.5" r="3.5" fill="none" stroke="#aaa" stroke-width="1.3"/><line x1="7" y1="7" x2="10" y2="10" stroke="#aaa" stroke-width="1.3"/></svg>
  </div>
  <div class="abs social" aria-label="Social links"><span></span><span></span><span></span><span></span></div>
</header>

<nav class="abs nav">
  <a>THE KVR</a><a>LOGISTICS</a><a>MARKET ANALYSIS</a><a>COMMUNITY</a><a>MEDIA</a><a>ABOUT US</a><a>REGIONAL TEAM</a><a>CONTACT US</a>
</nav>

<section class="abs hero" role="img" aria-label="Businesswoman touching a world map with arrows linking locations"></section>
<div class="abs quote-top"></div>
<div class="abs quote-mid"></div>
<div class="abs quote-text">"KVR ASSOCIATES KVR<br><span class="light">A </span>LOREST<span class="light">, NESTO </span>LACUSFEMENTINE IGIDO<span class="light">"</span></div>
<div class="abs quote-sub">Lorem ipsum dolor sit amet, consectetur adipiscing elit. Vestibulum id .</div>
<div class="abs more">MORE DETAILS</div>
<div class="abs dots"><i></i><i></i><i></i></div>

<section class="abs center">
  <h2>The Center Word Wide</h2>
  <article class="service" style="left:25px">
    <div class="pic" role="img" aria-label="Container ship at sea" style="background:linear-gradient(#4a6d84,#2f4e63)"></div>
    <h3>Daryage Calculator</h3>
    <p class="compact">Lacus fermentum ultrices ut eu turpis. Quisque sodales turpis ut risus dignissim non auctor velit malesuada. Nunc tristique mi ac turpis placerat quis sollicitudin</p>
    <a>Read More</a>
  </article>
  <article class="service" style="left:282px">
    <div class="pic" role="img" aria-label="Truck loading at a cargo plane" style="background:linear-gradient(#d4dbe3,#6f737a)"></div>
    <h3>Interactive Trade Map</h3>
    <p>Lacus fermentum ultrices ut eu turpis. Quisque sodales turpis ut risus dignissim non auctor velit malesuada.</p>
    <a>Read More</a>
  </article>
  <article class="service" style="left:540px">
    <div class="pic" role="img" aria-label="White delivery truck on the road" style="background:linear-gradient(#e6e8ea,#8f9296)"></div>
    <h3>SIte Map</h3>
    <p>Lacus fermentum ultrices ut eu turpis. Quisque sodales turpis ut risus dignissim non auctor velit malesuada.</p>
    <a>Read More</a>
  </article>
</section>

<section class="abs welcome">
  <h2 class="section-title">Welcome to KVR Associates</h2>
  <p>Contrairement à une opinion répandue, le Lorem Ipsum n'est pas simplement du texte aléatoire. Il trouve ses racines dans une oeuvre de la littérature latine classique datant de 45 av. J.-C., le rendant vieux de 2000 ans.Un professeur du Halbrook College, en Virginie, s'est intéressé à un des mots latins les plus obscurs, consectetur.</p>
  <p>Extrait d'un passage du Lorem Ipsum, et en étudiant tous les usages de ce mot dans la littérature classique, découvrit la source incontestable du Lorem Ipsum. Il provient en fait des sections 1.10.32 et 1.10.33 du "De Finibus Bonorum et Malorum" (Des Suprêmes Biens et des Suprêmes Maux) de Cicéron.</p>
  <a class="btn">Read More</a>
</section>

<section class="abs testimonials">
  <h2 class="section-title">Testimonials</h2>
  <div class="testimonial">
    <div class="avatar" role="img" aria-label="Portrait of a client"></div>
    <div><p>Plusieurs variations de Lorem Ipsum peuvent être trouvées ici ou là</p><p class="name">Marten Coley</p></div>
  </div>
  <div class="testimonial">
    <div class="avatar" role="img" aria-label="Portrait of a client"></div>
    <div><p>Plusieurs variations de Lorem Ipsum peuvent être trouvées ici ou là</p></div>
  </div>
  <a class="btn">Read More</a>
</section>

<footer class="abs footer">
  <div class="copy">© Copyrights 2014 All rights Reserved</div>
  <div class="follow">Socialize With Us : <span></span><span></span><span></span></div>
</footer>

</body>
</html>
```